Jewelry shop redesign

Would like to have my webshop (www.morvani.ee) to be redesigned. The shop system, which is built in AJAX will stay the same (consists of different widgets that can be placed using html), just the surroundings needs a luxurious and clean appearance. Only things needed to keep: friendspace like box, new product slideshow (can be redesigned aswell), the 3 links on the top which lead to information pages (can be made into buttons), the footer and of course the shop system widgets. The header picture/logo will need to be a link to homepage, which will be the main part of the design. I am quite keen to the display pic that i have on the fs page www.facebook.com/kaunistuspood, can be used to make a logo for the header, but feel free to do whatever, as long as it is CLEAN, SIMPLE, LUXURIOUS. get rid of the calculator...

widgets to use with the design (all not needed):

Product Browser Widget Code:
<div>
<script type="text/javascript" src="http://app.shopnix.com/script.js?718264" charset="utf-8"></script>
<script type="text/javascript"> xProductBrowser("categoriesPerRow=3","views=grid(3,3) list(10) table(20)","categoryView=grid","searchView=list","style="); </script>
<noscript>Your browser does not support JavaScript. Please proceed to <a href="http://morvani.shopnix.com">HTML version of Morvani OÜ</a></noscript>
</div>

Bag Widget Code:
<div>
<!- remove layout parameter if you want to position minicart yourself ->
<script type="text/javascript"> xMinicart("style=","layout=attachToCategories"); </script>
</div>

minicart: 
<div> <script type="text/javascript" src="http://app.shopnix.com/script.js?718264"></script> <script type="text/javascript"> xMinicart("style="); </script> </div>

Categories Tabs Widget Code:
<div>
<script type="text/javascript"> xCategories("style="); </script>
</div>

Categories Menu Widget Code:
<div>
<script type="text/javascript"> xVCategories("style="); </script>
</div>

Search Box Widget Code:
<div>
<script type="text/javascript"> xSearchPanel("style="); </script>
</div>

Target Market(s)

women, avg age 24

Industry/Entity Type

Shop

Requirements
Must have
• fs likebox, new product (UUED TOOTED) slideshow, keep the footer (just the company txt and pics), 3 information pages, shop widgets
Should not have
• the lease calculator.

```html
<!DOCTYPE html>
<html lang="en">
<head>
<meta charset="utf-8">
<title>Jewelry Shop</title>
<link rel="stylesheet" href="https://fonts.googleapis.com/css2?family=Tinos:ital,wght@0,400;0,700;1,400;1,700&family=Niconne&display=swap">
<style>
:root{
  --page-bg:#e6e7e6;
  --page-glow:#ffffff;
  --frame:#ffffff;
  --nav-top:#4a4b4f;
  --nav-bottom:#55575a;
  --hero-dark:#3c3f3f;
  --hero-mid:#6a6d6c;
  --nav-text:#ffffff;
  --tab-top:#6e7074;
  --tab-bottom:#3f4044;
  --heading:#4a4a4a;
  --orange:#f18a0a;
  --red:#d81f3d;
  --charcoal:#45464a;
  --rule:#c9caca;
}
*{margin:0;padding:0;box-sizing:border-box}
html,body{width:1200px;height:838px;overflow:hidden}
body{
  position:relative;
  background:
    radial-gradient(ellipse 560px 230px at 600px 600px,var(--page-glow) 0%,rgba(255,255,255,0.6) 50%,rgba(255,255,255,0) 100%),
    linear-gradient(180deg,#e9e9e9 0%,#eeeeee 30%,#f6f6f6 45%,#e4e5e4 100%);
  font-family:"Tinos","Times New Roman",serif;
}
.hero-shadow{
  position:absolute;left:120px;top:500px;width:960px;height:120px;
  background:radial-gradient(ellipse at center,rgba(0,0,0,0.14) 0%,rgba(0,0,0,0) 70%);
}
.hero{
  position:absolute;left:146px;top:37px;width:912px;height:499px;
  background:var(--frame);padding:4px;
  box-shadow:0 0 3px rgba(0,0,0,0.15);
}
.hero-inner{position:relative;width:100%;height:100%;overflow:hidden;background:var(--hero-dark)}
.hero-photo{
  position:absolute;inset:0;
  background:
    radial-gradient(ellipse 380px 140px at 470px 420px,#b9c0c4 0%,rgba(150,160,165,0.5) 45%,rgba(0,0,0,0) 100%),
    radial-gradient(circle 80px at 490px 390px,#8fb7cc 0%,rgba(143,183,204,0) 100%),
    linear-gradient(180deg,var(--hero-mid) 0%,#565958 45%,var(--hero-dark) 100%);
}
.nav{
  position:absolute;left:0;top:0;width:100%;height:90px;
  background:linear-gradient(180deg,var(--nav-top) 0%,var(--nav-bottom) 100%);
  border-bottom:1px solid #6c6e70;
}
.nav-notch{position:absolute;left:362px;top:89px}
.nav a{
  position:absolute;top:32px;color:var(--nav-text);text-decoration:none;
  font-weight:700;font-style:italic;font-size:15px;line-height:19px;text-align:center;
  text-shadow:0 1px 1px rgba(0,0,0,0.5);
}
.nav a.is-active{
  left:12px;top:32px;width:100px;height:27px;padding-top:4px;border-radius:4px 4px 0 0;
  background:linear-gradient(180deg,var(--tab-top),var(--tab-bottom));
}
.slider-cap{position:absolute;left:373px;top:443px}
.offer{
  position:absolute;left:444px;top:546px;width:317px;height:144px;background:#fff;
}
.offer-rule{position:absolute;top:613px;height:1px;background:var(--rule)}
.offer-rule.left{left:279px;width:165px}
.offer-rule.right{left:761px;width:163px}
.offer-svg{position:absolute;left:0;top:0}
.categories{position:absolute;left:0;top:698px;width:1200px}
.category{position:absolute;top:0;width:181px;text-align:center}
.category h2{
  font-weight:400;font-style:italic;font-size:27px;color:var(--heading);line-height:32px;white-space:nowrap;
  margin-left:-30px;margin-right:-30px;
}
.category .thumb{
  margin-top:12px;height:140px;border:4px solid #fff;box-shadow:0 0 2px rgba(0,0,0,0.2);
}
</style>
</head>
<body>
<div class="hero-shadow"></div>

<section class="hero">
  <div class="hero-inner">
    <div class="hero-photo" role="img" aria-label="Close-up photo of a silver ring set with a pale blue gemstone and a row of clear diamonds on a dark grey background"></div>
    <nav class="nav">
      <a class="is-active" href="#">Home</a>
      <a href="#" style="left:144px">Products</a>
      <a href="#" style="left:246px">About Us</a>
      <a href="#" style="left:596px">Contact Us</a>
      <a href="#" style="left:706px;width:64px">Discount Offers</a>
      <a href="#" style="left:809px">Feed Back</a>
    </nav>
    <svg class="nav-notch" width="172" height="26" viewBox="0 0 172 26" aria-hidden="true">
      <path d="M0 0 Q30 0 50 12 Q86 32 122 12 Q142 0 172 0 Z" fill="#55575a"/>
      <path d="M0 0.5 Q30 0.5 50 12.5 Q86 32.5 122 12.5 Q142 0.5 172 0.5" fill="none" stroke="#6c6e70"/>
    </svg>
    <svg class="slider-cap" width="200" height="50" viewBox="0 0 200 50" aria-label="Slideshow controls">
      <path d="M0 50 Q4 0 100 0 Q196 0 200 50 Z" fill="#fff"/>
      <circle cx="85" cy="25" r="15" fill="#222"/>
      <circle cx="118" cy="25" r="15" fill="#222"/>
      <path d="M89 17 L81 25 L89 33" fill="none" stroke="#fff" stroke-width="1.5"/>
      <path d="M114 17 L122 25 L114 33" fill="none" stroke="#fff" stroke-width="1.5"/>
    </svg>
  </div>
</section>

<div class="offer-rule left"></div>
<div class="offer-rule right"></div>
<div class="offer">
  <svg class="offer-svg" width="317" height="144" viewBox="0 0 317 144" aria-label="Today's offer: 30% offer, click here">
    <circle cx="55" cy="78" r="52" fill="#d9d9d9"/>
    <circle cx="53" cy="73" r="52" fill="var(--orange)"/>
    <circle cx="53" cy="73" r="49" fill="none" stroke="#f7a53c" stroke-width="1"/>
    <circle cx="269" cy="78" r="50" fill="#d9d9d9"/>
    <circle cx="267" cy="73" r="50" fill="var(--charcoal)"/>
    <circle cx="159" cy="76" r="67" fill="#d0d0d0"/>
    <circle cx="157" cy="71" r="66" fill="var(--red)"/>
    <circle cx="157" cy="71" r="62" fill="none" stroke="#e44a63" stroke-width="1"/>
    <text x="55" y="72" text-anchor="middle" fill="#fff" font-family="Tinos,serif" font-weight="700" font-size="15">TODAY`S</text>
    <text x="55" y="90" text-anchor="middle" fill="#fff" font-family="Tinos,serif" font-weight="700" font-size="15">OFFER:</text>
    <text x="156" y="58" text-anchor="middle" fill="#fff" font-family="Niconne,cursive" font-size="18">30 %</text>
    <text x="156" y="92" text-anchor="middle" fill="#fff" font-family="Niconne,cursive" font-size="28">Offer</text>
    <text x="266" y="72" text-anchor="middle" fill="#fff" font-family="Tinos,serif" font-weight="700" font-size="15" text-decoration="underline">CLICK</text>
    <text x="266" y="90" text-anchor="middle" fill="#fff" font-family="Tinos,serif" font-weight="700" font-size="15" text-decoration="underline">HERE!</text>
    <line x1="243" y1="74" x2="290" y2="74" stroke="#fff" stroke-width="1"/>
    <line x1="243" y1="92" x2="290" y2="92" stroke="#fff" stroke-width="1"/>
  </svg>
</div>

<section class="categories">
  <div class="category" style="left:150px">
    <h2>Rings</h2>
    <div class="thumb" role="img" aria-label="Photo of a vintage diamond brooch with leaf branches on a dark background" style="background:linear-gradient(160deg,#3a403d,#5a5f5a 60%,#8a8b84)"></div>
  </div>
  <div class="category" style="left:378px">
    <h2>Other Product</h2>
    <div class="thumb" role="img" aria-label="Photo of a dark textured metal band ring on a grey gradient" style="background:linear-gradient(180deg,#7c7e82,#d4d5d7 60%,#f0f0f0)"></div>
  </div>
  <div class="category" style="left:607px">
    <h2>Product 3</h2>
    <div class="thumb" role="img" aria-label="Photo of crystal earrings and a necklace displayed on cream fabric" style="background:linear-gradient(170deg,#7a6456,#c4b4a4 50%,#e6ddd2)"></div>
  </div>
  <div class="category" style="left:836px">
    <h2>Product 4</h2>
    <div class="thumb" role="img" aria-label="Photo of a turquoise flower necklace and earrings on a white display bust" style="background:linear-gradient(170deg,#d8cfbe,#c3b8a3 50%,#b9d2d6)"></div>
  </div>
</section>
</body>
</html>
```